Flyer für Unterstützung in der Personalarbeit
Zielgruppe
HR Freelancer, bitte Dienstleistung für Unternehmen an, die temporär Unterstützung in der Personalarbeit (Personalprozesse, Recruiting, Lohn- und Gehaltsabrechnung, HR Management, Administration) benötigen.
Aufgabenstellung
Ich benötige einen mehrseitigen Flyer, der mich und meine Arbeit kurz vorstellt. Außerdem soll es in einem Teil darum gehen, warum ein HR Freelancer eine gute Wahl ist. Der Flyer/die Broschüre soll an Unternehmen versendet werden.
Ich wünsche mir ein modernes minimalistisches und dennoch ansprechendes Design. Ich benötige die Datei am Ende auch im Word Format, da ich zukünftig Referenzen und weitere Auftraggeber ergänzen muss.
Ich füge zudem verschiedene Bilder bei, dabei müssen nicht alle berücksichtigt werden.

```html
<!DOCTYPE html>
<html lang="de">
<head>
<meta charset="utf-8">
<title>Lena Marwitz – HR Freelancerin Broschüre</title>
<link rel="stylesheet" href="https://fonts.googleapis.com/css2?family=Poppins:wght@500;600;700&family=Nunito:wght@400;600;700&family=Quicksand:wght@400;500&display=swap">
<style>
:root{
  --red:#e8523f;
  --red-dark:#d9442f;
  --pink:#fdeeec;
  --ink:#1e1e1e;
  --text:#333;
  --paper:#fff;
  --stage:#eceff1;
  --photo-a:#cfc8c0;
  --photo-b:#8e8a84;
}
*{box-sizing:border-box;margin:0;padding:0}
html,body{width:857px;height:1200px;overflow:hidden;background:var(--stage)}
body{position:relative;font-family:"Nunito",sans-serif;color:var(--text)}
.page{position:absolute;width:654px;height:926px;background:var(--paper);transform:scale(.5285);transform-origin:0 0;overflow:hidden;box-shadow:0 2px 10px rgba(0,0,0,.08)}
.p1{left:67px;top:111px}.p2{left:431px;top:111px}
.p3{left:67px;top:621px}.p4{left:431px;top:621px}
.abs{position:absolute}
h2,h3{font-family:"Poppins",sans-serif}
.red{color:var(--red)}
.ticks{list-style:none}
.ticks li{position:relative;padding-left:22px;font-size:11px;line-height:1.5}
.ticks li::before{content:"";position:absolute;left:0;top:2px;width:14px;height:14px;border-radius:50%;background:var(--red)}
.ticks li::after{content:"";position:absolute;left:5px;top:4.5px;width:3px;height:6px;border:solid #fff;border-width:0 2px 2px 0;transform:rotate(45deg)}
.dots{list-style:none}
.dots li{position:relative;padding-left:13px}
.dots li::before{content:"";position:absolute;left:0;top:6px;width:5px;height:5px;border-radius:50%;background:currentColor}
.photo{position:absolute}
.footer-tab{position:absolute;left:0;bottom:0}
.page-no{position:absolute;bottom:6px;right:34px;color:#fff;font:700 20px "Poppins",sans-serif}

/* page 1 */
.p1 .photo{left:0;top:0;width:654px;height:750px;background:linear-gradient(160deg,#e9e7e4 0%,#bdb8b1 45%,#8b877f 100%)}
.brand-box{left:372px;top:0;width:256px;height:228px;background:var(--red);border-radius:0 0 26px 26px;color:#fff;text-align:center;font-family:"Quicksand",sans-serif;padding-top:104px}
.brand-name{font-size:36px;font-weight:400;line-height:1}
.brand-tag{font-size:17px;font-weight:400;margin-top:18px;letter-spacing:.5px}
.name-band{left:0;top:718px;width:342px;height:62px;background:var(--red);border-radius:0 32px 32px 0;color:#fff;font:700 39px/62px "Poppins",sans-serif;padding-left:55px}
.cover-title{left:56px;top:800px;font:700 36px/1.22 "Poppins",sans-serif;color:var(--red)}

/* page 2 */
.p2 .wall{left:0;top:0;width:654px;height:345px;background:linear-gradient(90deg,#f6f5f4,#ecebea)}
.p2 .photo{left:400px;top:70px;width:254px;height:492px;background:linear-gradient(180deg,#c9b8a6,#3a3a3e 55%,#5e6f86)}
.hello{left:60px;top:118px;font:600 21px "Poppins",sans-serif;color:var(--ink)}
.hello span{color:var(--red)}
.intro{left:60px;top:170px;width:310px;font-size:11px;line-height:20px;color:var(--ink)}
.contact{left:0;top:345px}
.contact-title{left:60px;top:372px;font:600 20px "Poppins",sans-serif;color:#fff}
.contact-list{left:0;top:408px;list-style:none;color:#fff;font-family:"Quicksand",sans-serif;font-size:13px}
.contact-list li{position:relative;height:25.3px;padding-left:85px;line-height:22px}
.contact-list li::before{content:"";position:absolute;left:0;top:5px;width:76px;height:12px;background:#fff;border-radius:0 7px 7px 0}
.contact-list .ico{position:absolute;left:58px;top:3px;width:16px;height:16px}
.expertise-title{left:60px;top:592px;font:600 21px "Poppins",sans-serif;color:var(--red)}
.expertise{left:60px;top:637px}
.expertise li{margin-bottom:8.3px}

/* page 3 */
.p3-inner{position:absolute;left:51px;top:68px;width:560px}
.career-title{font:600 19px/1.2 "Poppins",sans-serif;color:var(--ink);margin-bottom:18px}
.career-title span{color:var(--red)}
.station{position:relative;margin-bottom:12px}
.station h3{position:relative;font-size:14px;font-weight:600;color:var(--red);margin-bottom:6px}
.station h3::before{content:"";position:absolute;left:-51px;top:10px;width:42px;height:1px;background:var(--red)}
.station .ticks li{margin-bottom:3px;font-size:10.5px}
.cols{display:flex;gap:40px}
.cols>div{flex:1}
.sub{font:700 10.5px "Nunito",sans-serif;color:var(--ink);margin-bottom:4px}
.traits{position:absolute;left:0;top:760px;width:654px;height:166px;background:var(--pink);padding:28px 51px}
.traits h3{font-size:14px;font-weight:600;color:var(--red);margin-bottom:8px}
.traits li{margin-bottom:4px;font-size:10.5px}
.traits b{color:var(--red);font-weight:600}

/* page 4 */
.services{position:absolute;left:49px;top:62px;width:270px}
.services h2{font-size:19px;font-weight:600;color:var(--ink);margin-bottom:10px}
.services h2 span{color:var(--red)}
.svc{color:var(--red);margin-bottom:11px}
.svc h3{font:600 10.5px/1.3 "Poppins",sans-serif;color:var(--red)}
.svc p{color:var(--ink);font-size:10.5px;line-height:1.6;margin-top:3px}
.frame-panel{left:320px;top:0;width:334px;height:215px;background:var(--red);color:#fff;padding:62px 30px 0}
.frame-panel h2{font-size:18px;font-weight:600;margin-bottom:10px}
.frame-panel li{font-size:10.5px;line-height:1.6;margin-bottom:8px}
.why-panel{left:320px;top:215px;width:334px;height:600px;background:var(--pink);padding:28px 30px 0;color:var(--red)}
.why-panel h2{font-size:18px;font-weight:600;color:var(--ink);margin-bottom:10px}
.why-panel h2 span{color:var(--red)}
.why-panel h3{font:600 10.5px "Poppins",sans-serif;color:var(--red)}
.why-panel p{color:var(--ink);font-size:10.5px;line-height:1.6;margin:4px 0 11px}
.cta-shape{left:0;top:780px}
.cta{left:317px;top:806px;width:315px;color:#fff}
.cta h3{font-size:13px;font-weight:600;line-height:1.3;margin-bottom:6px}
.cta p{font-size:10px;line-height:1.65}
</style>
</head>
<body>

<!-- Cover -->
<section class="page p1">
  <div class="photo" role="img" aria-label="Porträtfoto der HR-Freelancerin am Flussufer vor moderner Stadtarchitektur"></div>
  <div class="abs brand-box">
    <div class="brand-name">Lena Marwitz</div>
    <div class="brand-tag">HR Freelancer</div>
  </div>
  <div class="abs name-band">Lena Marwitz</div>
  <h1 class="abs cover-title">Ihre HR-Freelancerin für<br>maßgeschneiderte Lösungen</h1>
</section>

<!-- Intro / Kontakt / Expertise -->
<section class="page p2">
  <div class="abs wall"></div>
  <svg class="abs contact" width="654" height="217" viewBox="0 0 654 217"><path d="M0 0 H300 Q390 0 420 60 V217 H0 Z" fill="var(--red)"/></svg>
  <div class="photo" role="img" aria-label="Porträtfoto der HR-Freelancerin im dunklen Blazer an einer hellen Wand"></div>
  <h2 class="abs hello"><span>Hallo, ich bin</span> Lena Marwitz</h2>
  <p class="abs intro">Ich bin eine HR-Generalistin mit über <span class="red">10 Jahren Erfahrung.</span> Als HR-Freelancerin helfe ich Unternehmen dabei, ihre HR-Prozesse zu optimieren und maßgeschneiderte Lösungen zu finden. Ob Personalbetreuung, Recruiting oder Prozessverbesserungen – ich kenne die Herausforderungen und packe sie mit Leidenschaft an.</p>
  <h2 class="abs contact-title">Kontakt</h2>
  <ul class="abs contact-list">
    <li><svg class="ico" viewBox="0 0 16 16"><circle cx="8" cy="8" r="8" fill="var(--red)"/><path d="M5.2 4.5l1.6-.4.9 2-1 .8a5 5 0 0 0 2.4 2.4l.8-1 2 .9-.4 1.6c-3.4.3-6.6-2.9-6.3-6.3z" fill="#fff"/></svg>0176 / 48 15 62 90 (Messenger)</li>
    <li><svg class="ico" viewBox="0 0 16 16"><circle cx="8" cy="8" r="8" fill="var(--red)"/><rect x="4" y="5" width="8" height="6" rx="1" fill="#fff"/><path d="M4.3 5.5 8 8.3l3.7-2.8" stroke="var(--red)" fill="none" stroke-width=".9"/></svg>mail@lenamarwitz.de</li>
    <li><svg class="ico" viewBox="0 0 16 16"><circle cx="8" cy="8" r="8" fill="var(--red)"/><circle cx="8" cy="8" r="3" fill="#fff"/></svg>Lena Marwitz</li>
    <li><svg class="ico" viewBox="0 0 16 16"><circle cx="8" cy="8" r="8" fill="var(--red)"/><path d="M8 3.5a3 3 0 0 1 3 3c0 2.2-3 5.8-3 5.8S5 8.7 5 6.5a3 3 0 0 1 3-3z" fill="#fff"/><circle cx="8" cy="6.5" r="1.1" fill="var(--red)"/></svg>Falkenhain, Berlin</li>
    <li><svg class="ico" viewBox="0 0 16 16"><circle cx="8" cy="8" r="8" fill="var(--red)"/><circle cx="8" cy="8" r="3.6" fill="none" stroke="#fff" stroke-width="1.1"/><path d="M4.4 8h7.2M8 4.4v7.2" stroke="#fff" stroke-width=".8"/></svg>Webseite: lenamarwitz.de</li>
  </ul>
  <h2 class="abs expertise-title">Expertise</h2>
  <ul class="abs ticks expertise">
    <li>HR Generalist / Personalbetreuung</li>
    <li>Full Life Cycle Recruiting</li>
    <li>Einführung und Betreuung von Bewerbermanagementsystemen</li>
    <li>Vorbereitende Lohn- und Gehaltsabrechnung (Kalvio)</li>
    <li>Zusammenarbeit mit Arbeitnehmervertretungen</li>
    <li>Berufserfahrung in verschiedenen Dienstleistungsbranchen</li>
    <li>Fließende Englischkenntnisse</li>
  </ul>
  <svg class="footer-tab" width="654" height="46" viewBox="0 0 654 46"><path d="M0 38 H530 Q552 38 562 19 Q572 0 598 0 H654 V46 H0 Z" fill="var(--red)"/></svg>
  <span class="page-no">02</span>
</section>

<!-- Berufliche Stationen -->
<section class="page p3">
  <div class="p3-inner">
    <h2 class="career-title"><span>Berufliche Stationen und</span><br>relevante Projekterfahrung</h2>
    <div class="station">
      <h3>HR-Freelancerin (seit 2024)</h3>
      <div class="cols">
        <div>
          <p class="sub">Interim HR Operations:</p>
          <ul class="ticks">
            <li>Betreuung eines Unternehmens mit ca. 10.000 Mitarbeitenden</li>
            <li>Bearbeitung von HR Operations Anfragen</li>
            <li>Beratung in übergreifenden HR Prozessen zu Disziplinarmaßnahmen, Bescheinigungswesen und Verträgen</li>
          </ul>
        </div>
        <div>
          <p class="sub">Senior HR Freelancer:</p>
          <ul class="ticks">
            <li>Unterstützung eines Online-Marketing-Unternehmens mit ca. 200 Mitarbeitenden</li>
            <li>Beratung hinsichtlich operativer Personalthemen</li>
            <li>Optimierung des Onboardings und der Personalbetreuung</li>
          </ul>
        </div>
      </div>
      <ul class="ticks" style="margin-top:4px">
        <li>Administrative und organisatorische Beratung der Teamleitung</li>
        <li>Beratung hinsichtlich der vor- und nachbereitenden Payroll</li>
      </ul>
    </div>
    <div class="station">
      <h3>HR-Generalistin bei Varnholt Service Solutions (2018 – 2023):</h3>
      <ul class="ticks">
        <li>Personalbetreuung und -verwaltung von ca. 650 Mitarbeitenden</li>
        <li>Vorbereitung von Lohn- und Gehaltsabrechnungen (Kalvio)</li>
        <li>Koordination von Personalvorgängen (Einstellungen, Vertragsänderungen, Austritte)</li>
        <li>Ansprechpartnerin für Mitarbeitende und Führungskräfte</li>
        <li>Durchführung des BEM-Prozesses zur Wiedereingliederung nach Krankheitszeiten</li>
      </ul>
    </div>
    <div class="station">
      <h3>Recruitment Manager bei Modekontor (2014 – 2018):</h3>
      <ul class="ticks">
        <li>Leitung des deutschlandweiten Recruitment-Teams</li>
        <li>Gesamtverantwortung für den Bewerbungsprozess: Stellenanzeigen, Auswahlgespräche</li>
        <li>Durchführung von High Volume Recruitings bei Neueröffnungen (ca. 300 Mitarbeitende)</li>
        <li>Unterstützung von Führungskräften bei der Rekrutierung und Teamaufbau</li>
      </ul>
    </div>
    <div class="station">
      <h3>HR Coordinator bei der Solbrück Hotelgruppe (2013 – 2014):</h3>
      <ul class="ticks">
        <li>Personaladministration und Bewerbermanagement</li>
        <li>Vorbereitende Lohnabrechnung und Unterstützung des externen Lohnbüros</li>
        <li>Pflege von Personalakten und Stammdaten</li>
        <li>Weiterentwicklung und Implementierung von HR-Prozessen</li>
      </ul>
    </div>
  </div>
  <div class="traits">
    <h3>Was mich auszeichnet</h3>
    <ul class="ticks">
      <li><b>Kommunikativ &amp; Organisiert:</b> Ich setze auf klare Kommunikation und strukturiertes Arbeiten.</li>
      <li><b>Empathisch &amp; Diskret:</b> Der respektvolle Umgang mit Menschen ist mir wichtig.</li>
      <li><b>Innovativ &amp; Teamfähig:</b> Immer offen für neue Ideen und eine starke Teamplayerin.</li>
    </ul>
  </div>
  <svg class="footer-tab" width="654" height="46" viewBox="0 0 654 46"><path d="M0 38 H530 Q552 38 562 19 Q572 0 598 0 H654 V46 H0 Z" fill="var(--red)"/></svg>
  <span class="page-no">03</span>
</section>

<!-- Leistungen / Rahmendaten -->
<section class="page p4">
  <div class="services">
    <h2><span>Leistungen</span> im Überblick</h2>
    <ul class="dots">
      <li class="svc"><h3>Interim HR &amp; Projektmanagement:</h3><p>Temporäre Übernahme von HR-Aufgaben zur Überbrückung von Vakanzen, Unterstützung in Projekten oder bei Engpässen.</p></li>
      <li class="svc"><h3>Onboarding-Prozesse:</h3><p>Gestaltung und Optimierung von Onboarding-Prozessen zur schnellen und effektiven Integration neuer Mitarbeiter.</p></li>
      <li class="svc"><h3>Recruiting &amp; High Volume Recruiting:</h3><p>Rekrutierung der passenden Talente für Ihr Unternehmen, inklusive vollständigem Bewerbermanagement und Vorstellungsgesprächen.</p></li>
      <li class="svc"><h3>Vorbereitende Abrechnung &amp; Payroll:</h3><p>Unterstützung bei Lohn- und Gehaltsabrechnungen, einschließlich Pflege von Daten in Kalvio und Zeiterfassungssystemen.</p></li>
      <li class="svc"><h3>Personalbetreuung &amp; Verwaltung:</h3><p>Umfassende Betreuung Ihrer Mitarbeiter und Sicherstellung reibungsloser Personalprozesse.</p></li>
      <li class="svc"><h3>Betriebliches Eingliederungsmanagement (BEM):</h3><p>Begleitung und Koordination von BEM-Prozessen zur erfolgreichen Wiedereingliederung nach längeren Krankheitsphasen.</p></li>
      <li class="svc"><h3>Zusammenarbeit mit Arbeitnehmervertretungen:</h3><p>Unterstützung bei der Kommunikation und Verhandlungen mit Betriebsräten zu arbeitsrechtlichen Themen.</p></li>
      <li class="svc"><h3>Organisationsentwicklung &amp; Prozessverbesserung:</h3><p>Analyse und Optimierung von Prozessen zur Steigerung der Effizienz und Flexibilität Ihres Unternehmens.</p></li>
    </ul>
  </div>
  <div class="abs frame-panel">
    <h2>Rahmendaten</h2>
    <ul class="dots">
      <li>Verfügbarkeit: Ab sofort, Teilzeit / Vollzeit, flexibel nach Absprache</li>
      <li>Einsatzort: Deutschlandweit remote, mit planbarer Reisetätigkeit. In Berlin/Brandenburg auch Hybrid möglich.</li>
    </ul>
  </div>
  <div class="abs why-panel">
    <h2><span>Warum ein</span> HR-Freelancer?</h2>
    <ul class="dots">
      <li><h3>Flexibilität</h3><p>Freelancer können stundenweise oder projektbezogen engagiert werden – man bezahlt nur für tatsächlich benötigte Leistungen.</p></li>
      <li><h3>Spezialisierte Expertise</h3><p>Sie bringen Fachwissen aus verschiedenen Branchen mit und bieten sofortige Lösungen für spezifische HR-Aufgaben.</p></li>
      <li><h3>Kosteneffizienz</h3><p>Keine Fixkosten für Sozialleistungen, nur flexible Bezahlung nach Aufwand.</p></li>
      <li><h3>Unabhängige Perspektive</h3><p>Externe Freelancer bringen frische Ideen und können Prozesse objektiv bewerten und optimieren.</p></li>
      <li><h3>Schnelle Verfügbarkeit</h3><p>Freelancer sind sofort einsatzbereit und unterstützen kurzfristig bei Engpässen oder Projekten.</p></li>
      <li><h3>Projektbezogene Unterstützung</h3><p>Sie übernehmen zeitlich begrenzte Aufgaben und Projekte, von der Planung bis zur Umsetzung.</p></li>
      <li><h3>Netzwerk und Erfahrung</h3><p>Durch Erfahrung in verschiedenen Unternehmen bieten sie wertvolle Kontakte und Best Practices.</p></li>
    </ul>
  </div>
  <svg class="abs cta-shape" width="654" height="146" viewBox="0 0 654 146"><path d="M0 146 V128 H200 Q250 128 268 70 Q290 0 360 0 H654 V146 Z" fill="var(--red)"/></svg>
  <div class="abs cta">
    <h3>Lassen Sie uns Ihre HR-Themen gemeinsam erfolgreich gestalten!</h3>
    <p>Kontaktieren Sie mich gerne für ein unverbindliches Gespräch – ich freue mich darauf, Ihre HR-Prozesse zu optimieren und Ihr Team erfolgreich zu unterstützen.</p>
  </div>
</section>

</body>
</html>
```